NEW Modern Sleek Business Card for VR Language Startup

Our startup is using VR to lead the next wave of world language education. We need a two-sided business card that introduces the larger organization (Quorvel Language Inc) and our contact info on one side and shows the product, Lumidrasca, on the other side.

Side 1 (contact info)= Quorvel Logo and Contact info (name, title, phone, email)

Side 2 (product)= Lumidrasc logo, text, and website
Text= Culturally Immersive Language Learning Games
Website= www.lumidrasc.example

Target Market(s)

Education, Technology

Contact Information for Business Card

Contact info will be updated upon approval of the design. For now, put this as a placeholder.

Perry Hollins
Founder & CEO
phollins@mailtrove.example
(555)-014-2736

Font styles to use
Other font styles liked:
• Gibson and Century Gothic are the brand fonts

Requirements
Nice to have
• I would love to see cohesion between the design and colors of the two logos. I have attached a few business card designs that I like, so you can get a feel for my preferred style.

```html
<!DOCTYPE html>
<html lang="en">
<head>
<meta charset="utf-8">
<title>Quorvel Language – Business Card</title>
<link href="https://fonts.googleapis.com/css2?family=Questrial&family=Tinos:wght@400;700&display=swap" rel="stylesheet">
<style>
  :root {
    --backdrop: #2b2b2d;
    --card: #f7f7f8;
    --ink: #2f3640;
    --ink-soft: #6b6f76;
    --accent-red: #e0344b;
    --link-blue: #2f52c8;
    --brand-slate: #3a4654;
    --wash-pink: #f7b7b0;
    --wash-lilac: #c6b8f0;
    --wash-mint: #b8ece4;
    --wash-sky: #bfe6f3;
    --wash-violet: #cfc6f2;
    --mark-blue: #3c86e6;
  }
  * { box-sizing: border-box; margin: 0; padding: 0; }
  html, body { width: 1200px; height: 997px; overflow: hidden; }
  body { background: var(--backdrop); position: relative; font-family: "Questrial", sans-serif; }

  .card {
    position: absolute;
    width: 620px;
    height: 354px;
    background: var(--card);
    border-radius: 4px;
    overflow: hidden;
    box-shadow: 0 18px 40px rgba(0,0,0,.45);
  }
  .card--contact { left: 60px; top: 110px; }
  .card--product { left: 520px; top: 500px; }

  .card__wash { position: absolute; border-radius: 50%; }
  .card--contact .card__wash {
    right: -70px; top: -120px; width: 460px; height: 460px;
    background: linear-gradient(160deg, var(--wash-pink) 0%, var(--wash-lilac) 60%, var(--wash-mint) 100%);
    opacity: .75;
  }
  .card--product .card__wash {
    left: 140px; top: -140px; width: 500px; height: 500px;
    background: linear-gradient(150deg, var(--wash-sky) 0%, var(--wash-violet) 100%);
    opacity: .7;
  }

  .brand { position: absolute; display: flex; align-items: center; gap: 12px; }
  .brand__dot { width: 38px; height: 38px; border-radius: 50%; background: var(--accent-red); }
  .brand__name { color: var(--brand-slate); font-family: "Questrial", sans-serif; }

  .card--contact .brand { left: 34px; top: 150px; }
  .card--contact .brand__name { font-size: 24px; letter-spacing: 3px; }

  .person { position: absolute; left: 34px; top: 210px; }
  .person__name { font-family: "Tinos", serif; font-weight: 700; font-size: 19px; color: var(--ink); }
  .person__title { font-family: "Tinos", serif; font-size: 13px; color: var(--ink-soft); }

  .contacts { position: absolute; left: 34px; top: 262px; list-style: none; }
  .contacts li { display: flex; align-items: center; gap: 12px; height: 24px; font-family: "Tinos", serif; font-size: 13px; color: var(--ink); }
  .contacts li.contacts__web { font-weight: 700; }
  .contacts svg { width: 20px; height: 20px; flex: none; }

  .card--product .brand { left: 0; right: 0; top: 130px; flex-direction: column; gap: 14px; }
  .card--product .brand__dot { width: 70px; height: 70px; background: var(--mark-blue); }
  .card--product .brand__name { font-size: 52px; }

  .tagline { position: absolute; left: 0; right: 0; top: 268px; text-align: center; font-family: "Tinos", serif; font-weight: 700; font-size: 17px; color: #111; }
  .website { position: absolute; left: 0; right: 0; top: 292px; text-align: center; font-family: "Tinos", serif; font-weight: 700; font-size: 19px; color: var(--link-blue); }
</style>
</head>
<body>

<section class="card card--contact" aria-label="Contact side">
  <div class="card__wash" role="img" aria-label="Soft pastel decorative wash"></div>
  <div class="brand">
    <span class="brand__dot"></span>
    <span class="brand__name">QUORVEL LANGUAGE</span>
  </div>
  <div class="person">
    <p class="person__name">Perry Hollins</p>
    <p class="person__title">Owner / Founder</p>
  </div>
  <ul class="contacts">
    <li>
      <svg viewBox="0 0 20 20"><circle cx="10" cy="10" r="10" fill="var(--accent-red)"/><path d="M6.5 5.5l2 0 1 2.5-1.3 1a6 6 0 0 0 2.8 2.8l1-1.3 2.5 1v2a1 1 0 0 1-1 1A8 8 0 0 1 5.5 6.5a1 1 0 0 1 1-1z" fill="#fff"/></svg>
      (555)-014-2736
    </li>
    <li>
      <svg viewBox="0 0 20 20"><circle cx="10" cy="10" r="10" fill="var(--accent-red)"/><rect x="5" y="6.5" width="10" height="7" fill="#fff"/><path d="M5 6.5l5 4 5-4" stroke="var(--accent-red)" stroke-width="1" fill="none"/></svg>
      phollins@mailtrove.example
    </li>
    <li class="contacts__web">
      <svg viewBox="0 0 20 20"><circle cx="10" cy="10" r="10" fill="var(--accent-red)"/><path d="M10 15.5s-4-4.2-4-7a4 4 0 0 1 8 0c0 2.8-4 7-4 7z" fill="#fff"/><circle cx="10" cy="8.5" r="1.5" fill="var(--accent-red)"/></svg>
      www.mailtrove.example
    </li>
  </ul>
</section>

<section class="card card--product" aria-label="Product side">
  <div class="card__wash" role="img" aria-label="Soft blue decorative wash"></div>
  <div class="brand">
    <span class="brand__dot"></span>
    <span class="brand__name">Lumidrasc</span>
  </div>
  <p class="tagline">Culturally Immersive Language Learning Games</p>
  <p class="website">www.lumidrasc.example</p>
</section>

</body>
</html>
```